Need new Spot UV Business Card design

We are looking for a new business card design incorporating Spot UV in black & white options / versions. See examples files and Tobin Ashgrove Design logo.
You can see our website at www.tobinashgrove.ca. We want something classy but yet modern. We are open to black or black and/or white on white with the spot uv. We are open to portrait or landscape. Size should be standard 3.5" x 2". The front of the card should focus on the logo and name "Tobin Ashgrove" only. Fonts used should be "Open sans" or "PT Sans".

Target Market(s)

Mid to high end

Industry/Entity Type

Business

Contact Information for Business Card

Tobin Velasko
416.382.4417
tobin@tobinashgrove.ca
www.tobinashgrove.ca
4175 Brightwell Blvd. E Suite 308
Mississauga, ON L5T 2K9

Requirements
Must have
• Name & Logo

```html
<!DOCTYPE html>
<html lang="en">
<head>
<meta charset="utf-8">
<title>Tobin Ashgrove — Business Card Drafts</title>
<link href="https://fonts.googleapis.com/css2?family=Open+Sans:wght@300;400;600;700&display=swap" rel="stylesheet">
<style>
  :root {
    --board: #1e1e1e;
    --card: #0b0b0b;
    --card-edge: #0e0e0e;
    --spot-uv: #161616;
    --spot-uv-line: #1c1c1c;
    --text-main: #f2f2f2;
    --silver: #bdbdbd;
    --caption: #6a6a6a;
  }
  * { margin: 0; padding: 0; box-sizing: border-box; }
  html, body {
    width: 1200px;
    height: 1200px;
    overflow: hidden;
    background: var(--board);
    font-family: "Open Sans", sans-serif;
  }
  .board {
    position: relative;
    width: 1200px;
    height: 1200px;
  }
  .card {
    position: absolute;
    width: 458px;
    height: 286px;
    background: var(--card);
    box-shadow: 0 6px 18px rgba(0, 0, 0, 0.45);
    overflow: hidden;
  }
  .card--back { background: var(--card-edge); }

  .spot-uv-frame {
    position: absolute;
    border: 6px solid var(--spot-uv-line);
    background: var(--spot-uv);
  }
  .spot-uv-frame::after {
    content: "";
    position: absolute;
    inset: 22%;
    background: #121212;
  }

  .contact {
    position: absolute;
    color: var(--text-main);
    font-size: 13.5px;
    line-height: 15.6px;
    font-weight: 400;
    letter-spacing: 0.2px;
  }
  .contact .name { font-weight: 700; letter-spacing: 0.5px; }
  .contact .gap { height: 15.6px; }
  .contact .gap--small { height: 13px; }

  .brand {
    position: absolute;
    display: flex;
    align-items: center;
    color: var(--silver);
    font-weight: 400;
    white-space: nowrap;
  }
  .brand-square {
    border: 2px solid var(--silver);
    flex: none;
  }
  .brand--inline {
    left: 0; right: 0; top: 126px;
    justify-content: center;
    gap: 8px;
    font-size: 31px;
    line-height: 34px;
  }
  .brand--inline .brand-square { width: 26px; height: 26px; }
  .brand--stacked {
    left: 0; right: 0; top: 98px;
    flex-direction: column;
    gap: 10px;
    font-size: 24px;
    line-height: 28px;
  }
  .brand--stacked .brand-square { width: 53px; height: 53px; }

  .caption {
    position: absolute;
    left: 206px;
    top: 586px;
    width: 820px;
    text-align: center;
    color: var(--caption);
    font-size: 14px;
    font-weight: 400;
    letter-spacing: 14px;
    line-height: 18px;
  }
</style>
</head>
<body>
<main class="board">

  <!-- Version one -->
  <section class="card card--back" style="left:536px; top:262px;">
    <div class="brand brand--inline">
      <span class="brand-square"></span>
      <span class="brand-name">TOBIN ASHGROVE</span>
    </div>
  </section>

  <section class="card card--front" style="left:202px; top:78px;">
    <div class="spot-uv-frame" style="left:294px; top:34px; width:126px; height:126px;"></div>
    <div class="contact" style="left:29px; top:176px;">
      <div class="name">Tobin Velasko</div>
      <div>416.382.4417</div>
      <div class="gap"></div>
      <div>tobin@tobinashgrove.ca</div>
      <div>www.tobinashgrove.ca</div>
    </div>
    <div class="contact" style="left:221px; top:224px;">
      <div>4175 Brightwell Blvd. E Suite 308</div>
      <div>Mississauga, ON L5T 2K9</div>
    </div>
  </section>

  <p class="caption">BUSINESS CARD - DRAFT DESIGN</p>

  <!-- Version two -->
  <section class="card card--back" style="left:536px; top:834px;">
    <div class="brand brand--stacked">
      <span class="brand-square"></span>
      <span class="brand-name">TOBIN ASHGROVE</span>
    </div>
  </section>

  <section class="card card--front" style="left:202px; top:650px;">
    <div class="spot-uv-frame" style="left:35px; top:36px; width:216px; height:218px;"></div>
    <div class="contact" style="left:222px; top:84px;">
      <div class="name">Tobin Velasko</div>
      <div>416.382.4417</div>
      <div class="gap"></div>
      <div>tobin@tobinashgrove.ca</div>
      <div>www.tobinashgrove.ca</div>
      <div class="gap gap--small"></div>
      <div>4175 Brightwell Blvd. E Suite 308</div>
      <div>Mississauga, ON L5T 2K9</div>
    </div>
  </section>

</main>
</body>
</html>
```